New Website Design for High Quality Sailing School

This client has revised it's logo and branding and wants to create a new website that delivers a high-quality compelling design. Please read the brief, wireframes, brand guidelines and logos really carefully before you start your design work.
Note that the winning designer, based on the homepage, will be expected to do the other internal page designs as a part of this project.

Target Market(s)

Mainly Young Adults (20-35), High Net Worth, Love Sailing and Adventures

Industry/Entity Type

Leisure

Number of Pages Required

5+ page

Font styles to use
Sans Serif
Other font styles liked:
• Hyperspace Race

Requirements
Must have
• Attention to detail, high quality designs, applying the new branding carefully, and clean as per the brief.
Nice to have
• Keep it simple, but use the imagery. Take a look at the sites they like.
Should not have
• Inconsistency in design theme

```html
<!DOCTYPE html>
<html lang="en">
<head>
<meta charset="utf-8">
<title>Meridian Sailing</title>
<link href="https://fonts.googleapis.com/css2?family=Saira:wght@300;400;500;600&display=swap" rel="stylesheet">
<style>
:root{
  --red:#ef3f2a;
  --ink:#222;
  --grey:#666;
  --light:#f5f5f4;
  --dark:#2a2828;
  --white:#fff;
}
*{margin:0;padding:0;box-sizing:border-box}
html,body{width:1200px;height:4979px;overflow:hidden}
body{font-family:"Saira",sans-serif;color:var(--ink);background:var(--white);position:relative}
.abs{position:absolute}
.red{color:var(--red)}
.btn{position:absolute;background:var(--red);color:var(--white);font-size:15px;letter-spacing:1px;display:flex;align-items:center;justify-content:center;gap:10px;text-transform:uppercase}
.section-title{position:absolute;left:0;width:1200px;text-align:center;font-size:32px;font-weight:400;text-transform:uppercase;letter-spacing:.5px}

/* header */
.site-header{top:0;left:0;width:1200px;height:90px;background:var(--white)}
.brand{left:58px;top:14px;width:90px;text-align:center;font-size:12px;font-weight:500;letter-spacing:1px}
.brand-dot{width:30px;height:30px;background:var(--red);margin:0 auto 6px;border-radius:50%}
.top-links{right:62px;top:14px;font-size:11px;letter-spacing:.5px;color:var(--ink)}
.main-nav{right:190px;top:60px;display:flex;gap:26px;font-size:12px;letter-spacing:.5px;text-transform:uppercase}

/* hero */
.hero{top:90px;left:0;width:1200px;height:624px;background:linear-gradient(180deg,#7d98b8 0%,#a8bdd1 28%,#3d7fa4 45%,#1f5f84 70%,#154866 100%)}
.hero-title{left:60px;top:158px;font-size:48px;font-weight:600;line-height:56px;color:var(--white);text-transform:uppercase}
.hero-panel{left:50px;top:350px;width:370px;height:125px;background:rgba(20,30,40,.55)}
.hero-sub{left:60px;top:432px;color:var(--white);font-size:17px;letter-spacing:1px}
.play{width:50px;height:50px;border-radius:50%;background:var(--white)}

/* stakes */
.stakes{top:714px;left:0;width:1200px;height:440px;background:linear-gradient(90deg,#f2f3f5 0%,#fbfbfb 60%,#fff 100%)}
.stakes-lines{position:absolute;left:0;width:1200px;text-align:center;font-size:15px}

/* photo trio */
.trio{top:1154px;left:0;width:1200px;height:396px;display:flex}
.trio-item{position:relative;height:396px}
.trio-item p{position:absolute;bottom:24px;left:30px;right:30px;text-align:center;color:var(--white);font-size:14px;line-height:21px;letter-spacing:.6px}

/* slider */
.slide{left:60px;top:1748px;width:1080px;height:419px;background:linear-gradient(180deg,#d9dde2 0%,#b7c2cc 45%,#4e6a86 75%,#8fa3b6 100%)}
.slide-caption{left:60px;top:2052px;width:710px;height:90px;background:rgba(239,63,42,.9);color:var(--white);padding:18px 26px}
.slide-caption h3{font-size:26px;font-weight:400;letter-spacing:.5px}
.slide-caption p{font-size:13px;margin-top:4px}
.dots{left:563px;top:2205px;display:flex;gap:6px}
.dots span{width:9px;height:9px;border-radius:50%;background:#ccc}
.dots span:first-child{background:var(--red)}

/* featured */
.featured{top:2296px;left:0;width:1200px;height:285px;background:var(--light)}
.press{top:142px;width:172px;height:69px;background:var(--white);display:flex;align-items:center;justify-content:center;font-size:22px;font-weight:600;color:#111}

/* how it works */
.step{top:2731px;width:253px;height:344px;border-radius:6px;overflow:hidden}
.step-num{width:34px;height:34px;border-radius:50%;background:var(--red);color:var(--white);font-size:14px;display:flex;align-items:center;justify-content:center}
.step h4{position:absolute;left:18px;top:227px;color:var(--white);font-size:17px;font-weight:400;text-transform:uppercase}
.step p{position:absolute;left:18px;right:18px;top:258px;color:#e4e4e4;font-size:12.5px;line-height:19px}
.connector{height:2px;background:var(--red);top:2908px}

/* cta */
.cta{left:150px;top:3152px;width:900px;height:306px;border:2px solid var(--red);border-radius:42px;overflow:hidden}
.cta-title{left:62px;top:70px;font-size:32px;line-height:42px;text-transform:uppercase}
.cta-photo{right:0;top:0;width:350px;height:306px;border-radius:150px 0 0 150px;background:linear-gradient(160deg,#6a8aa3 0%,#3f6f8a 45%,#26506a 100%)}

/* video band */
.video{top:3535px;left:0;width:1200px;height:449px;background:linear-gradient(135deg,#1d4b5c 0%,#2a6575 45%,#1a4655 100%)}

/* ebook */
.ebook-art{left:140px;top:4030px;width:410px;height:415px;background:linear-gradient(160deg,#f6e3de 0%,#dfe6ee 50%,#b6c6d6 100%);border-radius:12px}
.ebook-title{left:606px;top:4062px;font-size:32px;line-height:38px;text-transform:uppercase}
.ebook-copy{left:610px;width:360px;font-size:13.5px;line-height:21px;color:var(--grey)}

/* footer */
.site-footer{top:4535px;left:0;width:1200px;height:444px;background:var(--dark);color:#ddd}
.foot-col{top:50px}
.foot-col h5{font-size:16px;font-weight:400;color:var(--white);text-transform:uppercase;margin-bottom:20px}
.foot-col ul{list-style:none}
.foot-col li{font-size:12.5px;line-height:26.5px;padding-left:16px;position:relative}
.foot-col li::before{content:"";position:absolute;left:0;top:12px;width:4px;height:4px;background:var(--red);border-radius:50%}
.social{width:32px;height:32px;border:2px solid var(--red);border-radius:50%}
.legal{left:62px;top:360px;font-size:12.5px;line-height:28px}
</style>
</head>
<body>

<header class="site-header abs">
  <div class="brand abs"><div class="brand-dot"></div>MERIDIAN</div>
  <div class="top-links abs">BLOG &nbsp;|&nbsp; GALLERY &nbsp;|&nbsp; ABOUT US &nbsp;|&nbsp; CONTACT US</div>
  <nav class="main-nav abs"><span>Destination</span><span>Liveaboard Courses</span><span>Our Tribe</span><span>Online Masterclasses</span></nav>
  <div class="btn" style="left:1035px;top:46px;width:105px;height:44px;font-size:13px">Email Us</div>
</header>

<section class="hero abs" role="img" aria-label="Superyacht cruising on open blue sea under a cloudy sky">
  <div class="hero-panel abs"></div>
  <h1 class="hero-title abs">Embark on a<br>lifetime of<br><span class="red">adventures!</span></h1>
  <div class="btn" style="left:60px;top:375px;width:135px;height:40px">Email Now</div>
  <div class="hero-sub abs">LEARN TO SAIL IN A WEEK</div>
  <div class="play abs" style="left:1090px;top:545px">
    <svg width="50" height="50"><polygon points="20,15 36,25 20,35" fill="#ef3f2a"/></svg>
  </div>
</section>

<section class="stakes abs" role="img" aria-label="Faint sailboat sail rising over a pale sky">
  <h2 class="section-title" style="top:72px">The stakes <span class="red">are high</span></h2>
  <div class="stakes-lines" style="top:138px">Bored ?</div>
  <div class="stakes-lines" style="top:168px">Tired ?</div>
  <div class="stakes-lines" style="top:198px">Stressed ?</div>
  <div class="stakes-lines" style="top:232px">Feeling Trapped? STOP Dreaming of a life of Adventure, and start living it..</div>
  <h2 class="section-title" style="top:346px">Embark <span class="red">successfully</span></h2>
</section>

<section class="trio abs">
  <div class="trio-item" style="width:398px;background:linear-gradient(180deg,#6f8a6c 0%,#4d5e4a 50%,#2f3a3e 100%)" role="img" aria-label="Group of students holding sailing course books by the coast">
    <p>Gain the skills, experience and formal certifications to successfully embark on your sailing journey</p></div>
  <div class="trio-item" style="width:405px;background:linear-gradient(180deg,#e8913e 0%,#a65a32 40%,#3a3e4a 100%)" role="img" aria-label="Sailing instructor on deck at sunset">
    <p>You deserve an incredible adventure, award-winning instructors, sexy new sailboats and a fun learning environment</p></div>
  <div class="trio-item" style="width:397px;background:linear-gradient(180deg,#8ea6c2 0%,#5d7592 50%,#2e3b4c 100%)" role="img" aria-label="Large group of friends posing on a sailboat">
    <p>Enjoy sailing adventures with friends and family in exotic destinations</p></div>
</section>

<h2 class="section-title" style="top:1625px;line-height:42px">The ultimate liveaboard<br><span class="red">sailing courses</span></h2>
<div class="slide abs" role="img" aria-label="Sailor in a captain's cap holding a rope on a sailboat over glittering water"></div>
<div class="slide-caption abs">
  <h3>4,000+ ALUMNI SAILING THE WORLD</h3>
  <p>Here at Meridian, we help thousands of people turn their sailing dreams into a reality</p>
</div>
<div class="dots abs"><span></span><span></span><span></span><span></span><span></span></div>

<section class="featured abs">
  <h2 class="section-title" style="top:70px">As featured <span class="red">in</span></h2>
  <svg class="abs" style="left:92px;top:162px" width="14" height="28"><polyline points="12,2 2,14 12,26" fill="none" stroke="#444" stroke-width="2"/></svg>
  <div class="press abs" style="left:140px">Open Water</div>
  <div class="press abs" style="left:326px">Wander &amp; Rest</div>
  <div class="press abs" style="left:513px">Ledger</div>
  <div class="press abs" style="left:700px">Helm Weekly</div>
  <div class="press abs" style="left:887px">Harbor Post</div>
  <svg class="abs" style="left:1100px;top:162px" width="14" height="28"><polyline points="2,2 12,14 2,26" fill="none" stroke="#444" stroke-width="2"/></svg>
</section>

<h2 class="section-title" style="top:2655px">How it <span class="red">works</span></h2>
<div class="connector abs" style="left:313px;width:23px"></div>
<div class="connector abs" style="left:589px;width:22px"></div>
<div class="connector abs" style="left:864px;width:22px"></div>

<div class="step abs" style="left:60px;background:linear-gradient(180deg,#e8e4e0 0%,#9a8f86 45%,#3b3735 100%)" role="img" aria-label="Woman reading on a sofa">
  <div class="step-num abs" style="left:16px;top:160px">01</div>
  <h4>Connect with us</h4><p>What are your sailing goals and dreams? Sailing and boating experience?</p></div>
<div class="step abs" style="left:336px;background:linear-gradient(180deg,#9fc2e0 0%,#6f8fad 45%,#2f4356 100%)" role="img" aria-label="Sailboat with white sails on the sea">
  <div class="step-num abs" style="left:12px;top:160px">02</div>
  <h4>Plan your trip</h4><p>Together we work on a curated trip for you. Confirm destination, the vessel, timeframe and the instructor.</p></div>
<div class="step abs" style="left:611px;background:linear-gradient(180deg,#4b4e56 0%,#5e5650 45%,#24242a 100%)" role="img" aria-label="Students holding course books in a marina at night">
  <div class="step-num abs" style="left:12px;top:160px">03</div>
  <h4>Prepare</h4><p>Embark! We send you resources to help you start planning, studying and preparing for your trip</p></div>
<div class="step abs" style="left:886px;background:linear-gradient(180deg,#a9b9c9 0%,#4e7f92 40%,#3d5a3a 100%)" role="img" aria-label="Aerial view of a green bay with anchored boats">
  <div class="step-num abs" style="left:12px;top:160px">04</div>
  <h4>Embark</h4><p>Sail on the trip of a lifetime..</p></div>

<section class="cta abs">
  <h2 class="cta-title abs">Start your sailing<br><span class="red">journey now</span></h2>
  <div class="btn" style="left:60px;top:180px;width:188px;height:43px">
    <svg width="16" height="16" viewBox="0 0 24 24"><path d="M6.6 10.8a15 15 0 0 0 6.6 6.6l2.2-2.2a1 1 0 0 1 1-.25 11.4 11.4 0 0 0 3.6.6 1 1 0 0 1 1 1V20a1 1 0 0 1-1 1A17 17 0 0 1 3 4a1 1 0 0 1 1-1h3.5a1 1 0 0 1 1 1c0 1.25.2 2.45.6 3.6a1 1 0 0 1-.25 1z" fill="#fff"/></svg>800.555.0142</div>
  <div class="btn" style="left:254px;top:180px;width:143px;height:43px">
    <svg width="18" height="14" viewBox="0 0 18 14"><rect x="0" y="0" width="18" height="14" rx="2" fill="#fff"/><polyline points="1,1 9,8 17,1" fill="none" stroke="#ef3f2a" stroke-width="2"/></svg>Email Us</div>
  <div class="cta-photo abs" role="img" aria-label="Happy friends with course books on a boat deck"></div>
</section>

<section class="video abs" role="img" aria-label="Aerial view of small sailing dinghies racing on dark green water">
  <div class="abs" style="left:62px;top:42px;width:2px;height:370px;background:#fff"></div>
  <div class="play abs" style="left:82px;top:300px">
    <svg width="50" height="50"><polygon points="20,15 36,25 20,35" fill="#ef3f2a"/></svg>
  </div>
  <p class="abs" style="left:86px;top:362px;color:#fff;font-size:16px;line-height:22px;letter-spacing:.8px">3000+ amazing alumni successfully embark on<br>their own sailing Journeys.</p>
</section>

<div class="ebook-art abs" role="img" aria-label="Tablet displaying a sailing magazine cover beside a faint sail shape"></div>
<h2 class="ebook-title abs">Receive your free<br><span class="red">e-book</span></h2>
<p class="ebook-copy abs" style="top:4150px">We've run so many courses, we know exactly what is needed to turn you from a sailor into a Skipper.</p>
<p class="ebook-copy abs" style="top:4235px">Here are our 5 Top Tips to help you successfully embark on your sailing journey.</p>
<div class="btn" style="left:612px;top:4300px;width:162px;height:42px">
  <svg width="18" height="14" viewBox="0 0 18 14"><rect x="0" y="0" width="18" height="14" rx="2" fill="#fff"/><polyline points="1,1 9,8 17,1" fill="none" stroke="#ef3f2a" stroke-width="2"/></svg>Email Now</div>

<footer class="site-footer abs">
  <div class="foot-col abs" style="left:62px"><h5>Destina<span class="red">tions</span></h5>
    <ul><li>Sea of Cortez Mexico</li><li>Grenadines, Caribbean</li><li>Bahamas, Caribbean</li><li>Tahiti, South Pacific</li><li>Mallorca, Spain</li><li>Trogir, Croatia</li><li>Bespoke Trips</li></ul></div>
  <div class="foot-col abs" style="left:337px"><h5>Disc<span class="red">over</span></h5>
    <ul><li>Liveaboard Courses</li><li>Our Tribe</li><li>Online Masterclasses</li><li>Instructors</li><li>Boats</li></ul></div>
  <div class="foot-col abs" style="left:612px"><h5>Expl<span class="red">ore</span></h5>
    <ul><li>Blog</li><li>Gallery</li><li>About Us</li><li>Contact Us</li></ul></div>
  <div class="foot-col abs" style="left:887px"><h5>Conn<span class="red">ect</span></h5>
    <div style="font-size:12.5px;line-height:26.5px">
      <div><svg width="16" height="12" style="vertical-align:middle;margin-right:14px"><rect width="16" height="12" rx="2" fill="#ef3f2a"/><polyline points="1,1 8,7 15,1" fill="none" stroke="#2a2828" stroke-width="1.5"/></svg>Email Us</div>
      <div><svg width="14" height="14" viewBox="0 0 24 24" style="vertical-align:middle;margin-right:16px"><path d="M6.6 10.8a15 15 0 0 0 6.6 6.6l2.2-2.2a1 1 0 0 1 1-.25 11.4 11.4 0 0 0 3.6.6 1 1 0 0 1 1 1V20a1 1 0 0 1-1 1A17 17 0 0 1 3 4a1 1 0 0 1 1-1h3.5a1 1 0 0 1 1 1c0 1.25.2 2.45.6 3.6a1 1 0 0 1-.25 1z" fill="#ef3f2a"/></svg>Call: +1 800.555.0142</div>
    </div>
  </div>
  <div class="social abs" style="left:887px;top:154px"></div>
  <div class="social abs" style="left:931px;top:154px"></div>
  <div class="social abs" style="left:975px;top:154px"></div>
  <div class="abs" style="left:887px;top:210px;width:62px;height:62px;border-radius:50%;background:#c8372a"></div>
  <div class="abs" style="left:965px;top:222px;width:20px;height:36px;background:var(--red)"></div>
  <div class="abs" style="left:995px;top:226px;font-size:15px;line-height:17px;color:var(--red);letter-spacing:2px">COASTAL<br>SAIL LEAGUE</div>
  <div class="abs" style="left:62px;top:348px;width:1076px;height:1px;background:#444"></div>
  <div class="legal abs">©Meridian Sailing, PO Box 1200, Pine Ridge, Colorado, 80000. - All Rights Reserved.<br>Sitemap &nbsp;&nbsp;|&nbsp;&nbsp; Terms of Use &nbsp;&nbsp;|&nbsp;&nbsp; Privacy Policy</div>
</footer>

</body>
</html>
```